conférence Débat Innovation
Bonjour,
Dans le cadre de l'organisation d'un événement institutionnel, je suis à la recherche d'un professionnel graphiste pour la création des supports suivants :
- flyer de l'événement (pour web et print),
- version pour les réseaux sociaux et le site internet de l'événement,
- flyer de cet événement personnalisé pour un concours dont la finale aura lieu le jour de l'événement,
- version affiches pour le jour J,
- Carton d'invitation pour mailing et impression.
L'événement est une conférence débat sur l'entreprenariat et l'innovation en banlieue parisienne.
L'idée est de dynamiser un territoire et le mettre en avant ses atouts.

```html
<!DOCTYPE html>
<html lang="fr">
<head>
<meta charset="utf-8">
<title>Conférence / Débat — Innovation</title>
<link rel="stylesheet" href="https://fonts.googleapis.com/css2?family=Open+Sans:wght@600;700;800&family=Arimo:wght@400&display=swap">
<style>
  :root {
    --paper: #ffffff;
    --ink: #111111;
    --orange: #f0a048;
    --blue: #7ea6f4;
    --blue-veil: rgba(126, 166, 244, 0.72);
    --texture-light: #f1f1f1;
    --texture-dark: #d6d6d6;
  }
  * { margin: 0; padding: 0; box-sizing: border-box; }
  html, body { width: 847px; height: 1200px; overflow: hidden; background: var(--paper); }
  .poster {
    position: relative;
    width: 847px;
    height: 1200px;
    overflow: hidden;
    background: var(--paper);
    font-family: "Open Sans", "Segoe UI", sans-serif;
    color: var(--ink);
  }
  .texture {
    position: absolute; inset: 0;
    background: linear-gradient(160deg, var(--texture-light) 0%, var(--texture-dark) 45%, var(--texture-light) 70%, var(--texture-dark) 100%);
    opacity: 0.8;
  }
  .block { position: absolute; }
  .block--orange-top { left: 88px; top: 80px; width: 402px; height: 404px; background: var(--orange); }
  .block--blue { left: 384px; top: 299px; width: 254px; height: 545px; background: var(--blue-veil); }
  .block--orange-bottom { left: 181px; top: 878px; width: 268px; height: 252px; background: var(--orange); }

  .bracket { position: absolute; }
  .bracket--top-left { left: 17px; top: 17px; }
  .bracket--venue-left { left: 268px; top: 695px; }
  .bracket--venue-right { left: 702px; top: 720px; }
  .bracket--bottom-right { left: 635px; top: 984px; }

  .more-info {
    position: absolute; left: 515px; top: 14px;
    font-size: 15px; font-weight: 700; letter-spacing: 0.3px;
  }
  .keyword {
    position: absolute;
    font-weight: 700;
    text-transform: uppercase;
    white-space: nowrap;
  }
  .keyword--entrepreneurship { left: 98px; top: 88px; font-size: 24px; letter-spacing: 4.5px; }
  .keyword--youth { left: 398px; top: 302px; font-size: 22px; letter-spacing: 9px; }
  .keyword--opportunity { left: 191px; top: 886px; font-size: 21px; letter-spacing: 3.6px; }
  .keyword--innovation { left: 333px; top: 1030px; font-size: 38px; letter-spacing: 14px; font-weight: 800; }

  .title {
    position: absolute; left: 66px; top: 512px; width: 720px;
    font-size: 71px; font-weight: 800; line-height: 1; white-space: nowrap;
    letter-spacing: -0.5px;
  }
  .subtitle {
    position: absolute; left: 80px; top: 592px;
    font-size: 27px; font-weight: 700; letter-spacing: 6.3px; white-space: nowrap;
  }
  .venue {
    position: absolute; right: 100px; top: 716px; text-align: right;
    font-family: "Arimo", Arial, sans-serif; line-height: 1.15;
  }
  .venue__place { font-size: 29px; }
  .venue__date { font-size: 19.5px; margin-right: 34px; }
</style>
</head>
<body>
<main class="poster">
  <div class="texture" role="img" aria-label="Fond gris texturé de fines hachures diagonales, d'engrenages et de trames de points"></div>

  <div class="block block--orange-top"></div>
  <div class="block block--orange-bottom"></div>
  <div class="block block--blue"></div>

  <svg class="bracket bracket--top-left" width="196" height="192" viewBox="0 0 196 192" aria-hidden="true">
    <rect x="0" y="0" width="196" height="22" fill="var(--blue)"/>
    <rect x="0" y="0" width="28" height="192" fill="var(--blue)"/>
  </svg>
  <svg class="bracket bracket--venue-left" width="78" height="79" viewBox="0 0 78 79" aria-hidden="true">
    <rect x="0" y="0" width="78" height="11" fill="var(--blue)"/>
    <rect x="0" y="0" width="11" height="79" fill="var(--blue)"/>
  </svg>
  <svg class="bracket bracket--venue-right" width="79" height="80" viewBox="0 0 79 80" aria-hidden="true">
    <rect x="0" y="69" width="79" height="11" fill="var(--orange)"/>
    <rect x="68" y="0" width="11" height="80" fill="var(--orange)"/>
  </svg>
  <svg class="bracket bracket--bottom-right" width="193" height="192" viewBox="0 0 193 192" aria-hidden="true">
    <rect x="0" y="167" width="193" height="25" fill="var(--orange)"/>
    <rect x="166" y="0" width="27" height="192" fill="var(--orange)"/>
  </svg>

  <p class="more-info">EN SAVOIR PLUS :</p>

  <p class="keyword keyword--entrepreneurship">Entreprenariat</p>
  <p class="keyword keyword--youth">Jeunesse</p>

  <h1 class="title">CONFÉRENCE / DÉBAT</h1>
  <p class="subtitle">MOMENT UNIQUE OUVERT A TOUS</p>

  <div class="venue">
    <p class="venue__place">HALLE DES RENCONTRES, PARIS</p>
    <p class="venue__date">21. SEPT 2016, À PARTIR DE 10H30</p>
  </div>

  <p class="keyword keyword--opportunity">Opportunité</p>
  <p class="keyword keyword--innovation">Innovation</p>
</main>
</body>
</html>
```